Tranquil Pathway Business Card

Logo attached. (will be printing onto thick white/off white textured card)

Double sided business card for two Therapists working at Tranquil Pathway.

Require one design, but with different name and mobile numbers on each card.

Target Market(s)

Medical, Health

Industry/Entity Type

Business

Contact Information for Business Card

Need one business card design, but a separate card for each person - Colin Marchetti and Marieke de Boeckx.

FRONT OF CARD

Logo

Name (Colin Marchetti on one card, Marieke de Boeckx on the other)
Professional Clinical Hypnotherapist

Consulting Rooms (Near Lindqvist Hospital)
482 Brackenfield Road
Dunmore VIC 3987

Colin@TranquilPathway.example.au OR Marieke@TranquilPathway.example.au

Mobile: 0455 872 604 (for Colin) OR
Mobile: 0467 290 518 (for Marieke)

BACK OF CARD

Logo

Website: www.TranquilPathway.example.au

Phone: 1300 958 471

Requirements
Must have
• Text and logo only. No additiional graphics.

```html
<!DOCTYPE html>
<html lang="en">
<head>
<meta charset="utf-8">
<title>Tranquil Pathway Business Card</title>
<link rel="stylesheet" href="https://fonts.googleapis.com/css2?family=Noto+Sans:wght@400;600&family=Arimo:wght@400&display=swap">
<style>
  :root {
    --page: #ffffff;
    --frame: #1a1a1a;
    --card-edge: #4a4a4a;
    --ink: #111111;
    --navy: #232a5c;
    --rule: #5f5f5f;
    --placeholder: #dcdcdc;
    --muted: #8a8a8a;
  }
  * { margin: 0; padding: 0; box-sizing: border-box; }
  html, body { width: 1200px; height: 1200px; overflow: hidden; background: var(--page); }
  .sheet {
    position: relative; width: 1200px; height: 1200px;
    border: 2px solid var(--frame); background: var(--page);
    font-family: "Noto Sans", sans-serif; color: var(--ink);
  }
  .card {
    position: absolute; left: 254px; width: 696px; height: 420px;
    border: 1px solid var(--card-edge); background: var(--page);
  }
  .card--front { top: 180px; }
  .card--back { top: 653px; }

  .brand { position: absolute; display: flex; align-items: center; }
  .brand__dot { border-radius: 50%; background: var(--placeholder); flex: none; }
  .brand__rule { background: var(--rule); flex: none; }
  .brand__name {
    font-family: "Noto Sans", sans-serif; font-weight: 600; color: var(--navy);
    text-transform: uppercase; line-height: 1.05;
  }
  .brand--small { left: 38px; top: 33px; }
  .brand--small .brand__dot { width: 64px; height: 64px; }
  .brand--small .brand__rule { width: 2px; height: 62px; margin: 0 8px; }
  .brand--small .brand__name { font-size: 17px; letter-spacing: 0.5px; }

  .brand--large { left: 0; right: 0; top: 116px; justify-content: center; }
  .brand--large .brand__dot { width: 134px; height: 134px; }
  .brand--large .brand__rule { width: 2px; height: 124px; margin: 0 18px; }
  .brand--large .brand__name { font-size: 36px; letter-spacing: 1px; }

  .holder { position: absolute; left: 0; right: 0; top: 170px; text-align: center; }
  .holder__name { font-size: 43px; font-weight: 400; line-height: 1.1; }
  .holder__role { font-size: 17px; margin-top: 2px; }

  .contact { position: absolute; left: 0; right: 0; top: 323px; text-align: center; font-size: 14.5px; }
  .contact__line { display: flex; justify-content: center; align-items: center; }
  .contact__item + .contact__item { border-left: 2px solid var(--ink); margin-left: 4px; padding-left: 4px; }
  .contact__address { margin-top: 9px; }

  .back-details {
    position: absolute; left: 0; right: 0; top: 328px; text-align: center;
    font-family: "Arimo", sans-serif; font-size: 14px; color: var(--muted); line-height: 24px;
  }
</style>
</head>
<body>
<div class="sheet">
  <section class="card card--front">
    <div class="brand brand--small">
      <span class="brand__dot"></span>
      <span class="brand__rule"></span>
      <span class="brand__name">Tranquil<br>Pathway</span>
    </div>
    <div class="holder">
      <p class="holder__name">Colin Marchetti</p>
      <p class="holder__role">Professional Clinical Hypnotherapist</p>
    </div>
    <div class="contact">
      <p class="contact__line">
        <span class="contact__item">0455 872 604</span>
        <span class="contact__item">Colin@TranquilPathway.example.au</span>
        <span class="contact__item">www.TranquilPathway.example.au</span>
      </p>
      <p class="contact__address">Consulting Rooms (Near Lindqvist Hospital) 482 Brackenfield Road Dunmore VIC 3987</p>
    </div>
  </section>

  <section class="card card--back">
    <div class="brand brand--large">
      <span class="brand__dot"></span>
      <span class="brand__rule"></span>
      <span class="brand__name">Tranquil<br>Pathway</span>
    </div>
    <div class="back-details">
      <p>www.TranquilPathway.example.au</p>
      <p>Phone: 1300 958 471</p>
    </div>
  </section>
</div>
</body>
</html>
```